Help our Crumb Parlour find our winning design! We're looking for a business card....

We’re a Crumb Parlour in NY specializing in custom-made cakes and unique desserts.
Our cakes combine flavor and art, each designed to match customer’s special event and theme.
We’d like a unique business card with a clean design that will combine French chic and artistic look & feel.
We’d like to differentiate ourselves from standard bakeries, please don’t offer cupcake images :-)
Our logo is peach-pink and brown and we’d love to use these colors ( . Another color that can be added is gold - or feel free to suggest!

Target Market(s)

Women, ages 25-55

Industry/Entity Type

Boutique

Contact Information for Business Card

Text on card:
Logo
Crumb Parlour by Dana Whitfield

www.xxxxxxxx.com
xxx@xxxxx.com
(516) xxx-xxxx
F – xxxxxxxxxx
IG - xxxxxxxxx

Font styles to use
Sans Serif
Script

Requirements
Must have
• Logo
• Clean look
• French chic and artistic look & feel.
Nice to have
• Damask pattern
Should not have
• Cupcake images

```html
<!DOCTYPE html>
<html lang="en">
<head>
<meta charset="utf-8">
<title>Crumb Parlour – Business Card</title>
<link rel="stylesheet" href="https://fonts.googleapis.com/css2?family=Great+Vibes&family=Lato:wght@300;400;700&display=swap">
<style>
  :root {
    --card-top: #eef0f1;
    --card-bottom: #e6e2de;
    --ink: #1c1a19;
    --peach: #c46a55;
    --band: #c87c69;
    --band-text: #f8e6df;
    --brand-brown: #4a2f27;
  }
  * { margin: 0; padding: 0; box-sizing: border-box; }
  html, body { width: 1200px; height: 930px; overflow: hidden; }
  body {
    background: linear-gradient(180deg, var(--card-top), var(--card-bottom));
    font-family: "Lato", "Helvetica Neue", Arial, sans-serif;
    color: var(--ink);
    position: relative;
  }
  .card { position: absolute; inset: 0; }
  .brand {
    position: absolute;
    left: 0; width: 1245px;
    top: 290px;
    text-align: center;
    font-family: "Lato", "Helvetica Neue", Arial, sans-serif;
    font-size: 50px;
    font-weight: 300;
    color: var(--brand-brown);
    letter-spacing: 2px;
    line-height: 1;
  }
  .brand-dot {
    display: inline-block;
    width: 14px; height: 14px;
    border-radius: 50%;
    background: var(--peach);
    margin-right: 18px;
    vertical-align: middle;
    position: relative; top: -4px;
  }
  .tagline, .handle, .phone {
    position: absolute;
    left: 0; width: 1245px;
    text-align: center;
    line-height: 1;
  }
  .tagline {
    top: 468px;
    font-family: "Great Vibes", "Brush Script MT", cursive;
    font-size: 42px;
    color: var(--ink);
  }
  .handle { top: 538px; font-size: 21px; font-weight: 700; color: var(--peach); letter-spacing: 0.3px; }
  .phone { top: 585px; font-size: 22px; font-weight: 400; }
  .contact-band {
    position: absolute;
    left: 178px; top: 632px;
    width: 891px; height: 64px;
    background: var(--band);
    opacity: 0.9;
    display: flex;
    align-items: center;
    justify-content: space-between;
    padding: 0 36px 0 34px;
    color: var(--band-text);
    font-size: 21px;
    font-weight: 400;
  }
  .contact-item { display: flex; align-items: center; gap: 14px; }
  .contact-icon { width: 22px; height: 22px; flex: none; }
</style>
</head>
<body>
  <main class="card">
    <div class="brand"><span class="brand-dot"></span>Velvet Crumb</div>

    <p class="tagline">Crumb Parlour by Dana Whitfield</p>
    <p class="handle">VelvetCrumbNYCakes</p>
    <p class="phone">(516) 555-0182</p>

    <div class="contact-band">
      <span class="contact-item">
        <svg class="contact-icon" viewBox="0 0 24 24" fill="none" stroke="currentColor" stroke-width="1.4" aria-hidden="true">
          <circle cx="12" cy="12" r="9.5"/>
          <ellipse cx="12" cy="12" rx="4.2" ry="9.5"/>
          <line x1="2.5" y1="12" x2="21.5" y2="12"/>
          <path d="M4.5 7h15M4.5 17h15"/>
        </svg>
        www.VelvetCrumbNY.com
      </span>
      <span class="contact-item">
        <svg class="contact-icon" viewBox="0 0 24 24" fill="none" stroke="currentColor" stroke-width="1.4" aria-hidden="true">
          <rect x="2.5" y="5.5" width="19" height="13"/>
          <path d="M2.5 5.5l9.5 7.5 9.5-7.5M2.5 18.5l7-6M21.5 18.5l-7-6"/>
        </svg>
        dana@VelvetCrumbNY.com
      </span>
    </div>
  </main>
</body>
</html>
```